Female Pest Controller needs awesome business cards

I need a logo design for a Pest Control service - something that appeals to 'nature' & safe, with the use of the colour green. I am also female
New Business Name is 'Bug Begone Bay'
appeals to women

Target Market(s)

Domestic Households & Local Businesses

Industry/Entity Type

Pest Control

Contact Information for Business Card

Corinne Waldrake
0428316952
ABN 47 618 259 304
PMT7314958207
Spiders Cockroaches, Ants, Silverfish, Fleas, Rodents

Font styles to use
Decorative

Colors
abd036
aaaaaa
5c5c5c

Requirements
Should not have
• Pics of dead insects, prefer nature inspired designs, frogs, trees etc
• Have attached old log & business name ( now my ex's business) Lilyvale Pest Solutions -

```html
<!DOCTYPE html>
<html lang="en">
<head>
<meta charset="utf-8">
<title>Bug Begone Bay — Business Card</title>
<link rel="stylesheet" href="https://fonts.googleapis.com/css2?family=Lato:wght@400;700&family=Arvo:wght@700&display=swap">
<style>
  :root {
    --green: #abd036;
    --grey-light: #aaaaaa;
    --grey-dark: #5c5c5c;
    --ink: #3c3c3c;
    --white: #ffffff;
  }
  * { margin: 0; padding: 0; box-sizing: border-box; }
  html, body { width: 1200px; height: 900px; overflow: hidden; }
  body {
    background: var(--grey-light);
    font-family: "Lato", Arial, sans-serif;
    position: relative;
  }
  .card {
    position: absolute;
    top: 200px;
    width: 310px;
    height: 502px;
  }
  .card--front {
    left: 253px;
    background: var(--white);
    border-radius: 62px 0 62px 0;
  }
  .card--back {
    left: 627px;
    background: var(--grey-dark);
    border-radius: 0 62px 0 62px;
  }
  .wordmark {
    position: absolute;
    display: flex;
    align-items: center;
    gap: 12px;
    font-family: "Lato", Arial, sans-serif;
    font-weight: 700;
    font-size: 34px;
    line-height: 1.05;
    color: var(--green);
  }
  .wordmark__dot {
    width: 40px;
    height: 40px;
    border-radius: 50%;
    background: var(--green);
    flex: none;
  }
  .card--front .wordmark { left: 38px; top: 160px; transform: translateY(-50%); }
  .card--back .wordmark { left: 34px; top: 252px; transform: translateY(-50%); }

  .holder-name {
    position: absolute;
    left: 33px;
    top: 338px;
    font-family: "Arvo", Georgia, serif;
    font-weight: 700;
    font-size: 20px;
    color: var(--grey-dark);
    white-space: nowrap;
  }
  .holder-name__first { color: var(--green); }

  .contact {
    position: absolute;
    left: 35px;
    top: 395px;
    list-style: none;
    font-size: 16px;
    line-height: 22px;
    color: var(--ink);
  }
  .contact__label { color: var(--green); margin-right: 4px; }

  .services {
    position: absolute;
    left: 0;
    right: 0;
    top: 411px;
    text-align: center;
    font-size: 16.5px;
    line-height: 21px;
    color: var(--white);
    white-space: nowrap;
  }
  .services__sep { color: var(--green); margin: 0 4px; }
</style>
</head>
<body>
  <section class="card card--front" aria-label="Business card front">
    <div class="wordmark">
      <span class="wordmark__dot" aria-hidden="true"></span>
      <span class="wordmark__name">Bug Begone<br>Bay</span>
    </div>
    <p class="holder-name"><span class="holder-name__first">Corinne</span> Waldrake</p>
    <ul class="contact">
      <li><span class="contact__label">Phone:</span> 0428316952</li>
      <li><span class="contact__label">ABN:</span> 47 618 259 304</li>
      <li><span class="contact__label">PMT Lic:</span> #73149582</li>
    </ul>
  </section>

  <section class="card card--back" aria-label="Business card back">
    <div class="wordmark">
      <span class="wordmark__dot" aria-hidden="true"></span>
      <span class="wordmark__name">Bug Begone<br>Bay</span>
    </div>
    <p class="services">
      Spiders<span class="services__sep">|</span>Cockroaches<span class="services__sep">|</span>Ants<br>
      Silverfish<span class="services__sep">|</span>Fleas<span class="services__sep">|</span>Rodents
    </p>
  </section>
</body>
</html>
```